CarWrap Varlo Kestrel K4M1 for a bouncy castle rental in Germany ("Leaping Domes Wendbach...

Dear ArtRally Community,

We operate a bouncy castle rental service in Crailsheim ("Springwelt Tauberfeld"), Germany. Customers have the option to rent bouncy castles for self-pickup. However, a portion of our customers also prefer to book a full-service package, which includes us traveling to the customer's location to set up, operate, and dismantle the bouncy castles on-site. In addition to bouncy castles, we also offer XXL outdoor games and fun food. For delivery purposes, we operate a Varlo Kestrel, which we would like to have wrapped with branding.

Vehicle:
Varlo Kestrel 2020 K4M1

Design Focus & Requirements:
- We are a startup and cannot yet afford a full vehicle wrap. Therefore, please focus the design on the blue highlighted areas as shown in the file "Focus Area for CarWrap.pdf". Note: The blue color is used solely to indicate the designated design areas - it is not a color requirement.
- Lettering and design elements may also extend beyond the blue areas.
- Both sides (left & right) should be designed, with focus on the highlighted areas.
- Front and rear of the vehicle may also include lettering/design elements.

Mandatory Design Elements:
- Logo must be included (see provided vector files)
- Website URL: springwelt-tauberfeld.de
- Slogan: "Rent Bouncy Castles" (German for "Rent Bouncy Castles")
- No phone number or address required
- Our Bouncy Castle flag ship is our "pirate ship Bouncy Castle"

Color & Branding:
- Please use the color palette from the provided logo vector files only
- Our Proud Main Color is Yellow. With Black and Magenta as Secondary Color.
- Reference file: "Colors Main and Secondary"
- Further references available on our website: https://springwelt-tauberfeld. de

Provided Files:
- Logos, fonts, images, and vector files of various products - all may be used
- Target design file: "Varlo Kestrel CarWrap Target file.ai" - please submit your final design adapted to this file

Technical Requirements:
- Final file format: AI (adapted from provided target file)
- Color mode: CMYK
- Resolution: minimum 300 DPI for any raster elements

For more information please let us know.

Target Market(s)

- easy to read while driving

Font styles to use
Serif
Other font styles liked:
• Our Fonts as in files provided

Requirements
Must have
• - Our logo, "Rent bouncy castles"
Nice to have
• Some colorful elements, we would like to be recognized very easily :-)
Should not have
• No full area car wrap (we can't afford that)

```html
<!DOCTYPE html>
<html lang="de">
<head>
<meta charset="utf-8">
<title>Springwelt Tauberfeld – Fahrzeugbeschriftung</title>
<link href="https://fonts.googleapis.com/css2?family=Montserrat:ital,wght@0,800;1,500&display=swap" rel="stylesheet">
<style>
  :root {
    --stage: #232323;
    --brand-yellow: #f7e15a;
    --brand-yellow-deep: #f2c51f;
    --ink: #111111;
    --magenta: #d9307a;
    --sky: #3aa0dc;
    --red: #e5452f;
    --sun: #fbd02c;
  }
  html, body {
    margin: 0;
    width: 711px;
    height: 1200px;
    overflow: hidden;
    background: var(--stage);
  }
  .canvas {
    position: relative;
    width: 711px;
    height: 1200px;
  }
  .hood-mark {
    position: absolute;
    left: 255px;
    top: 150px;
    width: 200px;
    text-align: center;
    font: 800 18px/1.1 "Montserrat", sans-serif;
    color: #ffffff;
    text-transform: uppercase;
    letter-spacing: 0.5px;
  }
  .hood-mark .dot {
    display: block;
    width: 36px;
    height: 36px;
    margin: 0 auto 8px;
    border-radius: 50%;
    background: var(--sun);
  }
  .side-panel {
    position: absolute;
    left: 30px;
    width: 651px;
    height: 170px;
  }
  .side-panel.right { top: 420px; }
  .side-panel.left { top: 820px; }
  .side-panel svg { display: block; }
  .brand-name {
    font: 800 30px "Montserrat", sans-serif;
    fill: var(--ink);
    text-transform: uppercase;
  }
  .slogan {
    font: italic 500 17px "Montserrat", sans-serif;
    fill: var(--ink);
  }
  .site-url {
    font: italic 500 14px "Montserrat", sans-serif;
    fill: var(--ink);
  }
</style>
</head>
<body>
<main class="canvas">

  <div class="hood-mark"><span class="dot"></span>Springwelt Tauberfeld</div>

  <!-- Passenger side -->
  <section class="side-panel right">
    <svg width="651" height="170" viewBox="0 0 651 170">
      <defs>
        <linearGradient id="panelFillR" x1="0" y1="0" x2="1" y2="0">
          <stop offset="0" stop-color="var(--brand-yellow)"/>
          <stop offset="1" stop-color="var(--brand-yellow-deep)"/>
        </linearGradient>
        <radialGradient id="castleFill" cx="0.5" cy="1" r="0.9">
          <stop offset="0" stop-color="#fff3a0"/>
          <stop offset="0.6" stop-color="var(--sun)"/>
          <stop offset="1" stop-color="#f0a623"/>
        </radialGradient>
        <linearGradient id="productFill" x1="0" y1="0" x2="1" y2="1">
          <stop offset="0" stop-color="#e9d24a"/>
          <stop offset="0.5" stop-color="#6cc04a"/>
          <stop offset="1" stop-color="#3aa0dc"/>
        </linearGradient>
      </defs>
      <rect class="panel-bg" x="2" y="2" width="647" height="166" rx="10" fill="url(#panelFillR)" stroke="#ffffff" stroke-width="2"/>
      <text class="brand-name" x="22" y="58">Springwelt</text>
      <text class="brand-name" x="22" y="92" font-size="24">Tauberfeld</text>
      <path class="swoosh" d="M18 160 Q120 110 300 118" fill="none" stroke="var(--magenta)" stroke-width="6"/>
      <path class="swoosh" d="M40 150 Q140 112 300 126" fill="none" stroke="var(--sky)" stroke-width="4"/>
      <text class="site-url" x="80" y="150">springwelt-tauberfeld.de</text>
      <text class="slogan" x="315" y="30">Hüpfburgen Mieten</text>
      <path role="img" aria-label="Illustration einer bunten Hüpfburg mit Türmen vor Sonnenstrahlen und Stadtsilhouette" d="M310 160 A70 70 0 0 1 450 160 Z" fill="url(#castleFill)"/>
      <rect role="img" aria-label="Foto einer großen bunten Hüpfburg mit Rutsche" x="470" y="48" width="170" height="108" rx="8" fill="url(#productFill)"/>
    </svg>
  </section>

  <!-- Driver side -->
  <section class="side-panel left">
    <svg width="651" height="170" viewBox="0 0 651 170">
      <defs>
        <linearGradient id="panelFillL" x1="1" y1="0" x2="0" y2="0">
          <stop offset="0" stop-color="var(--brand-yellow)"/>
          <stop offset="1" stop-color="var(--brand-yellow-deep)"/>
        </linearGradient>
      </defs>
      <rect class="panel-bg" x="2" y="2" width="647" height="166" rx="10" fill="url(#panelFillL)" stroke="#ffffff" stroke-width="2"/>
      <text class="slogan" x="130" y="30">Hüpfburgen Mieten</text>
      <rect role="img" aria-label="Foto einer großen bunten Hüpfburg mit Rutsche" x="10" y="40" width="160" height="108" rx="8" fill="url(#productFill)"/>
      <path role="img" aria-label="Illustration einer bunten Hüpfburg mit Türmen vor Sonnenstrahlen und Stadtsilhouette" d="M180 160 A70 70 0 0 1 320 160 Z" fill="url(#castleFill)"/>
      <text class="brand-name" x="350" y="58">Springwelt</text>
      <text class="brand-name" x="350" y="92" font-size="24">Tauberfeld</text>
      <path class="swoosh" d="M335 118 Q500 110 630 158" fill="none" stroke="var(--magenta)" stroke-width="6"/>
      <path class="swoosh" d="M335 126 Q490 116 610 160" fill="none" stroke="var(--sky)" stroke-width="4"/>
      <text class="site-url" x="350" y="152">springwelt-tauberfeld.de</text>
    </svg>
  </section>

</main>
</body>
</html>
```